A Dedicated Thank You to my Dad

Proposed Dimensions: Approx. 20" x 30"

For Father's Day, I wrote a dedication to my Dad that encapsulates my gratitude for everything he does, and everything he is. His birthday is on August 3, but it is more important for me to transform this dedication into a meaningful and memorable gift than to meet any deadline. I would love an image that captures the relationship between a father and his son, accompanied by my words of thanks in some sort of font that is appropriate for the message (calligprahy? not sure about that).

I had actually posted the Thank You on Chatterloop as a public post, so anyone with an account can read it: https://www.chatterloop.example/photo.php?fbid=20473819265038417&set=a.918364027159.5829361.3940582&type=1&theater

Only the words starting with "Thank you ..." should be on the poster.

Target Market(s)

This is a personal gift for my Dad. He doesn't have the best of eyesight, so having the words in a really small font would not be particularly helpful. :-)

Requirements
Must have
• * Personable
* Warm
* Inviting
* Memorable
* Understated more favored over Loud
Should not have
• * An entire palette of colors
* Wacky colors or fonts

```html
<!DOCTYPE html>
<html lang="en">
<head>
<meta charset="utf-8">
<title>Thank You — A Dedication</title>
<link href="https://fonts.googleapis.com/css2?family=Allura&family=Dancing+Script:wght@500;600&family=Open+Sans:wght@400;600&display=swap" rel="stylesheet">
<style>
  :root {
    --sea-top: #2a2f8f;
    --sea-mid: #a24fb8;
    --sea-pink: #e05aa8;
    --sea-low: #c44fb0;
    --card-top: #f6eef8;
    --card-mid: #f8eef4;
    --card-low: #f9dfd6;
    --card-edge: #ffffff;
    --title: #7a3a9e;
    --heading: #2b2372;
    --body: #3a3340;
    --ribbon: #8a55c0;
    --ribbon-dark: #6a3d9a;
    --ribbon-text: #ffffff;
    --photo-a: #7d8590;
    --photo-b: #c89a86;
    --photo-frame: #ffffff;
  }
  * { margin: 0; padding: 0; box-sizing: border-box; }
  html, body { width: 800px; height: 1200px; overflow: hidden; background: #ffffff; }
  .poster { position: relative; width: 800px; height: 1200px; overflow: hidden; }

  .backdrop {
    position: absolute; inset: 0;
    background: linear-gradient(160deg, var(--sea-pink) 0%, var(--sea-mid) 35%, var(--sea-top) 55%, var(--sea-mid) 80%, var(--sea-low) 100%);
  }
  .card { position: absolute; inset: 0; }

  .name-ribbon, .closing-ribbon { position: absolute; left: 0; top: 0; }
  .name-ribbon-text {
    position: absolute; top: 36px; left: 0; width: 800px; text-align: center;
    font: 600 15px/22px "Open Sans", sans-serif; letter-spacing: 0.5px; color: var(--ribbon-text);
  }
  .title {
    position: absolute; top: 62px; left: 0; width: 800px; text-align: center;
    font: 400 118px/120px "Allura", cursive; color: var(--title);
  }

  .photo {
    position: absolute; background: var(--photo-frame); padding: 8px;
    box-shadow: 0 2px 6px rgba(0,0,0,0.25);
  }
  .photo-fill { width: 100%; height: 100%; }
  .photo-left { left: 42px; top: 180px; width: 200px; height: 155px; transform: rotate(-3deg); }
  .photo-left .photo-fill { background: linear-gradient(135deg, #d9d5cc, var(--photo-a) 60%, #3d4552); }
  .photo-right { left: 588px; top: 138px; width: 188px; height: 228px; transform: rotate(5deg); }
  .photo-right .photo-fill { background: linear-gradient(160deg, #e3d6c4, var(--photo-b) 55%, #6b5a52); }

  .thanks { position: absolute; left: 0; width: 800px; text-align: center; top: var(--y); }
  .thanks-lead {
    display: block; font: 500 22px/24px "Dancing Script", cursive; color: var(--heading);
  }
  .thanks-detail {
    display: block; font: 400 13.5px/18px "Open Sans", sans-serif; color: var(--body);
  }
  .above-all {
    position: absolute; top: 1120px; left: 0; width: 800px; text-align: center;
    font: 400 13.5px/18px "Open Sans", sans-serif; color: var(--body);
  }
  .closing-text {
    position: absolute; top: 1139px; left: 0; width: 810px; text-align: center;
    font: 500 22px/28px "Dancing Script", cursive; color: var(--ribbon-text);
  }
</style>
</head>
<body>
<main class="poster">
  <div class="backdrop" role="img" aria-label="Sunset over the sea in pink, violet and deep blue tones"></div>

  <svg class="card" width="800" height="1200" viewBox="0 0 800 1200" aria-hidden="true">
    <defs>
      <linearGradient id="cardFill" x1="0" y1="0" x2="0" y2="1">
        <stop offset="0" stop-color="var(--card-top)"/>
        <stop offset="0.6" stop-color="var(--card-mid)"/>
        <stop offset="0.85" stop-color="var(--card-low)"/>
        <stop offset="1" stop-color="#f2c8d8"/>
      </linearGradient>
    </defs>
    <path d="M48 54 H752 A26 26 0 0 0 776 78 V1136 A26 26 0 0 0 752 1160 H48 A26 26 0 0 0 24 1136 V78 A26 26 0 0 0 48 54 Z"
          fill="url(#cardFill)" fill-opacity="0.93" stroke="var(--card-edge)" stroke-width="4"/>
  </svg>

  <svg class="name-ribbon" width="800" height="80" viewBox="0 0 800 80" aria-hidden="true">
    <polygon points="268,36 292,36 292,70 268,70 278,53" fill="var(--ribbon-dark)"/>
    <polygon points="532,36 556,36 546,53 556,70 532,70" fill="var(--ribbon-dark)"/>
    <rect x="282" y="32" width="262" height="30" fill="var(--ribbon)"/>
  </svg>
  <div class="name-ribbon-text">DAN HOLLOWAY</div>

  <h1 class="title">Thank You</h1>

  <figure class="photo photo-left"><div class="photo-fill" role="img" aria-label="Photo of father and son standing side by side indoors"></div></figure>
  <figure class="photo photo-right"><div class="photo-fill" role="img" aria-label="Photo of mother and father seated together at home"></div></figure>

  <p class="thanks" style="--y:203px"><span class="thanks-lead">Thank you for always carrying us</span><span class="thanks-detail">to the car after we fell asleep,<br>even after we were definitely old enough to walk it.</span></p>
  <p class="thanks" style="--y:268px"><span class="thanks-lead">Thank you for welcoming</span><span class="thanks-detail">more people to stay with us than I can count.</span></p>
  <p class="thanks" style="--y:315px"><span class="thanks-lead">Thank you for doggedly trying to teach me</span><span class="thanks-detail">that the beach is not to be feared nor cleaned.</span></p>
  <p class="thanks" style="--y:360px"><span class="thanks-lead">Thank you for loading us all up in the station wagon,</span><span class="thanks-detail">pillows in tow, so we could watch the first drive-in movie together and squint in the second.</span></p>
  <p class="thanks" style="--y:406px"><span class="thanks-lead">Thank you for, as coach, letting me</span><span class="thanks-detail">take a fake rabbit's foot onto the soccer field.</span></p>
  <p class="thanks" style="--y:456px"><span class="thanks-lead">Thank you for letting me sing in my room</span><span class="thanks-detail">as if I were the originating artist.</span></p>
  <p class="thanks" style="--y:503px"><span class="thanks-lead">Thank you for making car trips with you,</span><span class="thanks-detail">wherever we were going, fun and special.</span></p>
  <p class="thanks" style="--y:553px"><span class="thanks-lead">Thank you for putting up with the commutes you did,</span><span class="thanks-detail">for decades, so we could grow up amongst family and friends.</span></p>
  <p class="thanks" style="--y:601px"><span class="thanks-lead">Thank you for my dry sense of humor.</span><span class="thanks-detail">I cherish it.</span></p>
  <p class="thanks" style="--y:650px"><span class="thanks-lead">Thank you for finding a way, by hook or by crook,</span><span class="thanks-detail">to send three children to college at the same time.</span></p>
  <p class="thanks" style="--y:700px"><span class="thanks-lead">Thank you for never giving up on trying to convince me</span><span class="thanks-detail">that imperfection is not a failure.</span></p>
  <p class="thanks" style="--y:750px"><span class="thanks-lead">Thank you for teaching me</span><span class="thanks-detail">to try to find the good in everyone.</span></p>
  <p class="thanks" style="--y:796px"><span class="thanks-lead">Thank you for showing me</span><span class="thanks-detail">that there is peace to be found in stillness and quiet.</span></p>
  <p class="thanks" style="--y:845px"><span class="thanks-lead">Thank you for demonstrating</span><span class="thanks-detail">the fun that can be had and the truths that can be gleaned from debate.</span></p>
  <p class="thanks" style="--y:894px"><span class="thanks-lead">Thank you for accepting me for who I am,</span><span class="thanks-detail">no matter who I love, and for helping me to accept myself.</span></p>
  <p class="thanks" style="--y:941px"><span class="thanks-lead">Thank you for doing whatever you can to help whoever you can,</span><span class="thanks-detail">whether friend, family or stranger.</span></p>
  <p class="thanks" style="--y:989px"><span class="thanks-lead">Thank you for trusting me enough</span><span class="thanks-detail">to let your guard down to let me know how you are truly doing.</span></p>
  <p class="thanks" style="--y:1035px"><span class="thanks-lead">Thank you for insisting,</span><span class="thanks-detail">year after year, that time with you means more than any gift I could ever purchase.<br>That is one lesson, amongst so many, that I will pass down to our next generation.</span></p>

  <p class="above-all">Above all</p>

  <svg class="closing-ribbon" width="800" height="1200" viewBox="0 0 800 1200" aria-hidden="true">
    <polygon points="232,1142 258,1142 258,1176 232,1176 243,1159" fill="var(--ribbon-dark)"/>
    <polygon points="552,1142 578,1142 567,1159 578,1176 552,1176" fill="var(--ribbon-dark)"/>
    <rect x="246" y="1138" width="318" height="32" fill="var(--ribbon)"/>
  </svg>
  <p class="closing-text">Thank you for always being there.</p>
</main>
</body>
</html>
```